Design Creative Banner or Gif Ads. 3 Designs To Be Selected

Come up with some creative banner ads for stonewell.co.nz

*At least 3 different winning banners will be chosen*

Please provide banner ads / gif ads in common google ads / website banner formats.

They can be gif or static but must stand out while still maintaining clear clean text and visuals, with a premium professional feel (please avoid clip art or anything that gives a cheap message).

Please keep in mind that these will likely be small ads so text needs to be large and if there's there a lot of text then use multiple frames/ pages as submit as a gif.

Style
Minimal & clean lines
Architectural or realistic images
Avoid cartoon styles, clipart, or anything that looks cheap

Font
Nexa or Montserrat or similar

Tone
Premium, serious, trustworthy — fits new builds

Colours
Option 1: Deep Navy (trust & quality) & lighter blues and warm grey
Option 2: Open to bright colours to help the ads stand out, such as (but not limited to) bright pink with black, yellow, fluorescent green, provided the messaging is still done professionally.
Our logo is attached (Stone Well Logo)

Display Sizes
Ad specs for file sizes should be file formats like JPEG, GIF, and PNG, with animations limited to a max of 30 seconds or less.
We will need several different ad sizes provided for each of the 3 selected winning designs.

• Medium Rectangle: 300 × 250 pixels
• Leaderboard: 728 × 90 pixels
• Desktop Banner ad image: (640x360 pixels)
• Desktop Banner ad image 2: (300x600 pixels)
• Possibly one or two other sizes

Flexibility to be creative
The ad text, words, upper/lower case, layout, colour, theme, and images can be adjusted to how you think it will look best. The follow example ads are just examples of what we are after but we are keen to see what you can create.

Recommendations at this point:
1. Avoid text heavy
2. Looking for more Gif ads
3. Imaging: if possible use real stock photo's rather than AI

Themes:

1
Building Soon? Start Here
Free Build Planning Pack:
✓ Build Cost Calculator
✓ Hidden Cost Checklist
✓ Builder Comparison Guide
Build With Confidence
Download Free

2
Before You Choose A Builder
Compare Price, Scope, Risk & Value
Avoid Costly Mistakes
Choose The Right Builder With Confidence
Download The Free Guide

3
Planning A New Build?
Avoid These Common Mistakes:
✗ Hidden Exclusions
✗ Missing Scope
✗ Unrealistic Allowances
✗ Budget Blowouts
Download The Free Guide

4
Before You Buy Land
Know what it could cost to build.
Avoid Costly Building Mistakes
Download Our Free Guides

5
Know Your Build Budget?
• Free Build Cost Calculator
• Hidden Cost Checklist
• Build Planning Tools
Calculate Costs (Download)

Target Market(s)

Landowners looking to build

Industry/Entity Type

Building

Font styles to use
Other font styles liked:
• Nexa or Montserrat or similar

Requirements
Should not have
• Avoid cartoon styles, clipart, or anything that looks cheap

```html
<!DOCTYPE html>
<html lang="en">
<head>
<meta charset="utf-8">
<title>Stone Well – Banner Ads</title>
<link href="https://fonts.googleapis.com/css2?family=Poppins:wght@500;600;700&display=swap" rel="stylesheet">
<style>
  :root{
    --canvas:#5b5b5b;
    --navy:#0b2d4a;
    --navy-deep:#082640;
    --sky:#3aa2d6;
    --button:#3d9ad0;
    --white:#ffffff;
    --label:#ffffff;
  }
  *{box-sizing:border-box;margin:0;padding:0}
  html,body{width:1200px;height:1131px;overflow:hidden}
  body{background:var(--canvas);font-family:"Poppins",sans-serif;position:relative}
  .ad-label{position:absolute;top:36px;width:486px;text-align:center;color:var(--label);font-weight:500;font-size:30px;letter-spacing:1px}
  .ad{position:absolute;top:82px;height:971px;overflow:hidden;background:var(--navy)}
  .ad--one{left:81px;width:486px}
  .ad--two{left:633px;width:484px}
  .brand{position:absolute;left:0;top:0;width:100%;height:124px;background:var(--white);display:flex;align-items:center;justify-content:center;gap:22px}
  .brand__mark{width:62px;height:62px;background:var(--navy)}
  .brand__name{font-weight:600;font-size:44px;color:var(--navy);letter-spacing:-0.5px}
  .headline{position:absolute;left:51px;font-weight:700;line-height:1.15;color:var(--white)}
  .headline span{display:block;color:var(--sky)}
  .ad--one .headline{top:146px;font-size:40px}
  .ad--two .headline{top:158px;font-size:40px;line-height:1.3}
  .photo{position:absolute;inset:0;background:linear-gradient(180deg,#c9ccc9 0%,#a9a59d 35%,#3f4540 52%,#2f4a25 62%,#1d3216 100%)}
  .ad--one .photo{clip-path:polygon(0 332px,100% 221px,100% 527px,0 442px)}
  .ad--two .photo{clip-path:polygon(0 669px,100% 594px,100% 100%,0 100%)}
  .stripes{position:absolute;inset:0}
  .pack-title{position:absolute;left:51px;top:505px;font-weight:600;font-size:27px;line-height:1.32;color:var(--white)}
  .rule{position:absolute;height:3px;background:var(--sky)}
  .ad--one .rule{left:48px;top:585px;width:105px}
  .ad--two .rule{left:51px;top:273px;width:93px;background:var(--white)}
  .checklist{position:absolute;left:48px;top:606px;list-style:none}
  .checklist li{display:flex;align-items:center;gap:14px;height:34.5px;font-weight:600;font-size:21px;color:var(--white)}
  .checklist svg{width:28px;height:24px}
  .confidence{position:absolute;left:0;top:736px;width:100%;height:235px;background:var(--white)}
  .confidence__badge{position:absolute;left:102px;top:21px;width:72px;height:72px;border:3px solid var(--sky);border-radius:50%;display:flex;align-items:center;justify-content:center}
  .confidence__text{position:absolute;left:184px;top:20px;font-weight:500;font-size:31px;line-height:1.2;color:var(--navy)}
  .confidence__text span{display:block;color:var(--sky)}
  .cta{position:absolute;height:91px;border-radius:10px;background:var(--button);color:var(--white);display:flex;align-items:center;justify-content:center;gap:18px;font-weight:700}
  .ad--one .cta{left:26px;top:852px;width:432px;font-size:32px;gap:24px}
  .ad--two .cta{left:27px;top:852px;width:430px;font-size:22px;font-weight:600;gap:12px}
  .benefits{position:absolute;left:53px;top:318px;list-style:none;width:380px}
  .benefits li{display:flex;align-items:center;gap:20px;font-weight:500;font-size:20.5px;line-height:1.27;color:var(--white);height:94px;position:relative}
  .benefits li:not(:last-child)::after{content:"";position:absolute;left:86px;right:0;bottom:0;border-bottom:2px dashed var(--sky)}
  .benefits__icon{flex:0 0 65px;height:65px;border-radius:50%;background:radial-gradient(circle at 35% 30%,#3aa8dc,#1a6da3);display:flex;align-items:center;justify-content:center}
</style>
</head>
<body>
  <div class="ad-label" style="left:68px">AD 01</div>
  <div class="ad-label" style="left:627px">AD 02</div>

  <section class="ad ad--one">
    <div class="photo" role="img" aria-label="Modern dark gable-roof house on a grassy slope at dusk"></div>
    <svg class="stripes" viewBox="0 0 486 971" aria-hidden="true">
      <defs><linearGradient id="stripeA" x1="0" x2="1"><stop offset="0" stop-color="#1b6fa6"/><stop offset="1" stop-color="#3aa8dc"/></linearGradient></defs>
      <polygon points="0,325 486,213 486,222 0,334" fill="url(#stripeA)"/>
      <polygon points="0,438 486,522 486,532 0,447" fill="url(#stripeA)"/>
    </svg>
    <header class="brand"><div class="brand__mark"></div><div class="brand__name">Stone Well</div></header>
    <h1 class="headline">Building Soon?<span>Start Here</span></h1>
    <h2 class="pack-title">Free Build<br>Planning Pack:</h2>
    <div class="rule"></div>
    <ul class="checklist">
      <li><svg viewBox="0 0 28 24"><circle cx="12" cy="12" r="11" fill="#3aa2d6"/><path d="M7 12.5l3.5 3.5L17 9" stroke="#fff" stroke-width="2.4" fill="none" stroke-linecap="round"/></svg>Build Cost Calculator</li>
      <li><svg viewBox="0 0 28 24"><circle cx="12" cy="12" r="11" fill="#3aa2d6"/><path d="M7 12.5l3.5 3.5L17 9" stroke="#fff" stroke-width="2.4" fill="none" stroke-linecap="round"/></svg>Hidden Cost Checklist</li>
      <li><svg viewBox="0 0 28 24"><circle cx="12" cy="12" r="11" fill="#3aa2d6"/><path d="M7 12.5l3.5 3.5L17 9" stroke="#fff" stroke-width="2.4" fill="none" stroke-linecap="round"/></svg>Builder Comparison Guide</li>
    </ul>
    <div class="confidence">
      <div class="confidence__badge"><svg width="38" height="38" viewBox="0 0 38 38"><path d="M8 20l8 8L31 11" stroke="#0b2d4a" stroke-width="3.5" fill="none" stroke-linecap="round" stroke-linejoin="round"/></svg></div>
      <div class="confidence__text">Build With<span>Confidence</span></div>
    </div>
    <div class="cta">
      <svg width="40" height="38" viewBox="0 0 40 38"><path d="M20 3v22M11 16l9 9 9-9M4 24v10h32V24" stroke="#fff" stroke-width="4" fill="none" stroke-linecap="round" stroke-linejoin="round"/></svg>
      Download Free
    </div>
  </section>

  <section class="ad ad--two">
    <div class="photo" role="img" aria-label="Modern dark gable-roof house and cabin on a lawn at dusk"></div>
    <svg class="stripes" viewBox="0 0 484 971" aria-hidden="true">
      <defs><linearGradient id="stripeB" x1="0" x2="1"><stop offset="0" stop-color="#1b6fa6"/><stop offset="1" stop-color="#3aa8dc"/></linearGradient></defs>
      <polygon points="0,661 484,585 484,594 0,670" fill="url(#stripeB)"/>
    </svg>
    <header class="brand"><div class="brand__mark"></div><div class="brand__name">Stone Well</div></header>
    <h1 class="headline">Before You<span>Choose A Builder</span></h1>
    <div class="rule"></div>
    <ul class="benefits">
      <li><span class="benefits__icon"><svg width="34" height="34" viewBox="0 0 34 34"><circle cx="17" cy="17" r="12" stroke="#fff" stroke-width="2" fill="none"/><path d="M20.5 12.5c-1-1.2-6-1.6-6 1.4s6 1.6 6 4.6-5 2.8-6.5 1.2M17 9.5v15" stroke="#fff" stroke-width="2" fill="none" stroke-linecap="round"/></svg></span>Compare Price,<br>Scope, Risk &amp; Value</li>
      <li><span class="benefits__icon"><svg width="34" height="34" viewBox="0 0 34 34"><rect x="7" y="5" width="16" height="22" rx="2" stroke="#fff" stroke-width="2" fill="none"/><path d="M11 11h8M11 15h8M11 19h4" stroke="#fff" stroke-width="2"/><circle cx="24" cy="24" r="6" fill="#1a6da3" stroke="#fff" stroke-width="2"/><path d="M21.5 21.5l5 5M26.5 21.5l-5 5" stroke="#fff" stroke-width="2"/></svg></span>Avoid Costly<br>Mistakes</li>
      <li><span class="benefits__icon"><svg width="34" height="34" viewBox="0 0 34 34"><path d="M17 4l11 4v8c0 7-5 12-11 14C11 28 6 23 6 16V8z" stroke="#fff" stroke-width="2.2" fill="none" stroke-linejoin="round"/><path d="M12 17l4 4 7-7" stroke="#fff" stroke-width="2.4" fill="none" stroke-linecap="round"/></svg></span>Choose The Right<br>Builder With Confidence</li>
    </ul>
    <div class="cta">
      <svg width="34" height="34" viewBox="0 0 40 38"><path d="M20 3v22M11 16l9 9 9-9M4 24v10h32V24" stroke="#fff" stroke-width="4" fill="none" stroke-linecap="round" stroke-linejoin="round"/></svg>
      Download The Free Guide
    </div>
  </section>
</body>
</html>
```